Real estate agent : TJ Property

I have done the attached logo designed by your company .
My business card description as below:
Name : Daniel Ruiz
Mobile: 0491570156
Email : danielr@tjpropertyhq.net.au
Sales & Property Management

```html
<!DOCTYPE html>
<html lang="en">
<head>
<meta charset="utf-8">
<title>TJ Property – Business Card</title>
<link href="https://fonts.googleapis.com/css2?family=Montserrat:wght@700&family=Arimo:wght@400;700&display=swap" rel="stylesheet">
<style>
  :root {
    --backdrop: #1d1d1d;
    --card: #ffffff;
    --ink: #1a1a1a;
    --ink-soft: #2b2b2b;
  }
  html, body {
    margin: 0;
    width: 1200px;
    height: 988px;
    overflow: hidden;
    background: var(--backdrop);
  }
  .canvas {
    position: relative;
    width: 1200px;
    height: 988px;
  }
  .card {
    position: absolute;
    width: 620px;
    height: 354px;
    background: var(--card);
    border-radius: 22px;
    overflow: hidden;
    box-shadow: 0 10px 28px rgba(0,0,0,.5);
  }
  .card--front { left: 90px; top: 90px; }
  .card--back  { left: 490px; top: 544px; }

  .wordmark {
    font-family: "Montserrat", sans-serif;
    font-weight: 700;
    color: var(--ink);
    letter-spacing: 1px;
    white-space: nowrap;
  }
  .card--front .wordmark {
    position: absolute;
    left: 0; right: 0; top: 50%;
    transform: translateY(-50%);
    text-align: center;
    font-size: 58px;
  }
  .card--back .wordmark {
    position: absolute;
    left: 40px; top: 40px;
    font-size: 36px;
  }

  .person {
    position: absolute;
    left: 40px; top: 150px;
    font-family: "Arimo", sans-serif;
    color: var(--ink);
  }
  .person__name {
    margin: 0;
    font-weight: 700;
    font-size: 30px;
    letter-spacing: 1px;
    line-height: 1;
  }
  .person__role {
    margin: 6px 0 0;
    font-size: 17px;
    color: var(--ink-soft);
  }

  .contact {
    position: absolute;
    left: 40px; top: 248px;
    margin: 0; padding: 0;
    list-style: none;
    font-family: "Arimo", sans-serif;
    font-size: 18px;
    color: var(--ink);
  }
  .contact__item {
    display: flex;
    align-items: center;
    gap: 8px;
    height: 26px;
  }
  .contact__icon { width: 14px; height: 14px; flex: none; }
</style>
</head>
<body>
<main class="canvas">

  <section class="card card--front" aria-label="Card front">
    <div class="wordmark">TJ Property</div>
  </section>

  <section class="card card--back" aria-label="Card back">
    <div class="wordmark">TJ Property</div>

    <div class="person">
      <h1 class="person__name">DANIEL RUIZ</h1>
      <p class="person__role">Sales &amp; Property Management</p>
    </div>

    <ul class="contact">
      <li class="contact__item">
        <svg class="contact__icon" viewBox="0 0 16 16" aria-hidden="true">
          <path d="M3 1h3l1 4-2 1.5a9 9 0 0 0 4.5 4.5L11 9l4 1v3a2 2 0 0 1-2 2A12 12 0 0 1 1 3a2 2 0 0 1 2-2z" fill="var(--ink)"/>
        </svg>
        0491570156
      </li>
      <li class="contact__item">
        <svg class="contact__icon" viewBox="0 0 16 16" aria-hidden="true">
          <rect x="1" y="3" width="14" height="10" rx="1" fill="var(--ink)"/>
          <path d="M1.5 4l6.5 5 6.5-5" fill="none" stroke="var(--card)" stroke-width="1.3"/>
        </svg>
        danielr@tjpropertyhq.net.au
      </li>
      <li class="contact__item">
        <svg class="contact__icon" viewBox="0 0 16 16" aria-hidden="true">
          <circle cx="8" cy="8" r="7" fill="var(--ink)"/>
          <path d="M1 8h14M8 1c-3 3-3 11 0 14M8 1c3 3 3 11 0 14" fill="none" stroke="var(--card)" stroke-width="1"/>
        </svg>
        www.tjpropertyhq.net.au
      </li>
    </ul>
  </section>

</main>
</body>
</html>
```